Billboard Velmarhof - Maison K

I need two Billboards (125cm width x 340 height) -. They will be standing side by side in front of a building. Each billboard contains details of a business. 1. Medical center: VELMARHOF DRONSEL 2. Beauty saloon/Permanent make-up. MAISON K & ZOW Clinic. We already have a mockup. (see uploads). We want a design fitting the building with upmarket look. Modern, fresh and classy. The billboards need to have the same background color as in the mockup: dark-grey/black. The medical center has a green accent and the Beauty salon soft pink. The billboards should have certain uniformity.

Target Market(s)

Upmarket men and women

Font styles to use
Sans Serif

Requirements
Must have
• WE LIKE OUT OF THE BOX DESIGNS

VELMARHOF DRONSEL
Uw rug is onze zorg - this is the tagline
hello@velmarhofdronsel.be
09 614 28 90
www.velmarhofdronsel.be
facebook icon | instagram icon

MAISON K (HAS TWO DEPARTMENTS)
1. Schoonheidsinstituut - (which means beauty salon)
2. ZOW clinic (which means permanent make up)
0486 91 37 52
hello@maisonk.be
www.maisonk.be

hello@maisonk.be
Should not have
• not curly, not kitch, no color-books
NO PICTURES IN DESIGN

```html
<!DOCTYPE html>
<html lang="nl">
<head>
<meta charset="utf-8">
<title>Billboards Velmarhof Dronsel &amp; Maison K</title>
<link rel="stylesheet" href="https://fonts.googleapis.com/css2?family=Montserrat:wght@300;400;500&family=Oswald:wght@500;600&display=swap">
<style>
  :root {
    --canvas: #f2f2f2;
    --grid: #e4e4e4;
    --mount: #e6e6e6;
    --board: #3a3a3c;
    --green: #7fc64f;
    --pink: #f5e6e4;
    --ink-light: #ffffff;
    --ink-soft: #e9e4e2;
    --ink-grey: #bfbfbf;
    --rule: #8a8a8a;
    --line-dark: #2b2b2b;
  }
  * { margin: 0; padding: 0; box-sizing: border-box; }
  html, body { width: 1200px; height: 1200px; overflow: hidden; background: var(--canvas); }
  .presentation { position: relative; width: 1200px; height: 1200px; }
  .grid-line { position: absolute; background: var(--grid); }
  .grid-line.v { top: 0; width: 1px; height: 1200px; }
  .grid-line.h { left: 0; height: 1px; width: 1200px; }
  .mount { position: absolute; top: 133px; width: 361px; height: 930px; background: var(--mount); }
  .billboard { position: absolute; top: 144px; width: 343px; height: 912px; }
  .billboard svg { display: block; width: 100%; height: 100%; }
  .billboard--medical { left: 205px; background: var(--green); }
  .billboard--beauty { left: 650px; background: var(--pink); }
  .sans { font-family: 'Montserrat', sans-serif; }
  .condensed { font-family: 'Oswald', sans-serif; }
</style>
</head>
<body>
<main class="presentation">
  <div class="grid-line v" style="left:196px"></div>
  <div class="grid-line v" style="left:642px"></div>
  <div class="grid-line v" style="left:1003px"></div>
  <div class="grid-line h" style="top:133px"></div>
  <div class="grid-line h" style="top:1063px"></div>
  <div class="mount" style="left:196px"></div>
  <div class="mount" style="left:642px"></div>

  <!-- Medical centre board -->
  <section class="billboard billboard--medical">
    <svg viewBox="0 0 286 760" xmlns="http://www.w3.org/2000/svg">
      <path class="frame-outline" d="M13,68 Q143,-28 273,68 L273,692 Q143,788 13,692 Z" fill="none" stroke="var(--line-dark)" stroke-width="1.2"/>
      <path class="frame-panel" d="M25,76 Q143,-12 261,76 L261,686 Q143,770 25,686 Z" fill="var(--board)"/>
      <rect class="spine-decoration" role="img" aria-label="Faint spine decoration" x="100" y="110" width="110" height="540" rx="50" fill="#444446" opacity="0.45"/>

      <text class="brand-name sans" x="116" y="162" text-anchor="middle" font-size="20" font-weight="400" fill="var(--ink-light)">VELMARHOF</text>
      <text class="brand-sub sans" x="196" y="178" text-anchor="end" font-size="12" font-weight="400" fill="var(--ink-light)">DRONSEL</text>
      <circle class="brand-dot" cx="210" cy="165" r="5" fill="var(--green)"/>

      <g class="divider" stroke="var(--green)" stroke-width="0.8" fill="var(--green)">
        <line x1="92" y1="249" x2="192" y2="249"/><circle cx="92" cy="249" r="2"/><circle cx="192" cy="249" r="2"/>
        <line x1="92" y1="317" x2="192" y2="317"/><circle cx="92" cy="317" r="2"/><circle cx="192" cy="317" r="2"/>
        <line x1="144" y1="240" x2="144" y2="410"/>
        <line x1="144" y1="505" x2="144" y2="580"/>
      </g>
      <text class="tagline condensed" x="143" y="291" text-anchor="middle" font-size="24" font-weight="600" fill="var(--green)" letter-spacing="0.5">UW RUG IS ONZE ZORG</text>

      <g class="contact-rules" stroke="var(--rule)" stroke-width="0.6">
        <line x1="25" y1="427" x2="261" y2="427"/>
        <line x1="25" y1="445" x2="261" y2="445"/>
        <line x1="25" y1="484" x2="261" y2="484"/>
      </g>
      <g class="contact sans" font-size="11.5" fill="var(--ink-light)" text-anchor="middle" font-weight="300">
        <text x="143" y="440">www.velmarhofdronsel.be</text>
        <text x="143" y="461">09 614 28 90</text>
        <text x="143" y="478">hello@velmarhofdronsel.be</text>
      </g>
      <g class="socials sans" font-size="10" fill="var(--ink-soft)" text-anchor="middle" font-weight="400">
        <text x="109" y="609">instagram</text>
        <text x="178" y="609">facebook</text>
      </g>
    </svg>
  </section>

  <!-- Beauty salon board -->
  <section class="billboard billboard--beauty">
    <svg viewBox="0 0 286 760" xmlns="http://www.w3.org/2000/svg">
      <path class="frame-outline" d="M13,68 Q143,-28 273,68 L273,692 Q143,788 13,692 Z" fill="none" stroke="var(--line-dark)" stroke-width="1.2"/>
      <path class="frame-panel" d="M25,76 Q143,-12 261,76 L261,686 Q143,770 25,686 Z" fill="var(--board)"/>

      <circle class="brand-dot" cx="143" cy="84" r="6" fill="none" stroke="var(--ink-light)" stroke-width="1"/>
      <text class="brand-name sans" x="143" y="132" text-anchor="middle" font-size="12" font-weight="300" fill="var(--ink-light)" letter-spacing="6">MAISON K</text>
      <text class="brand-sub sans" x="143" y="147" text-anchor="middle" font-size="3.5" font-weight="400" fill="var(--ink-soft)" letter-spacing="2">SCHOONHEIDSINSTITUUT</text>

      <g class="divider" stroke="var(--ink-grey)" stroke-width="0.6" fill="var(--ink-light)">
        <line x1="100" y1="185" x2="186" y2="185"/><circle cx="100" cy="185" r="1.8"/><circle cx="186" cy="185" r="1.8"/>
        <line x1="100" y1="243" x2="186" y2="243"/><circle cx="100" cy="243" r="1.8"/><circle cx="186" cy="243" r="1.8"/>
        <line x1="144" y1="178" x2="144" y2="288"/>
        <line x1="100" y1="407" x2="186" y2="407"/><circle cx="100" cy="407" r="1.8"/><circle cx="186" cy="407" r="1.8"/>
        <line x1="144" y1="392" x2="144" y2="407"/>
        <line x1="100" y1="527" x2="186" y2="527"/><circle cx="100" cy="527" r="1.8"/><circle cx="186" cy="527" r="1.8"/>
        <line x1="100" y1="589" x2="186" y2="589"/><circle cx="100" cy="589" r="1.8"/><circle cx="186" cy="589" r="1.8"/>
        <line x1="144" y1="520" x2="144" y2="589"/>
        <line x1="144" y1="609" x2="144" y2="625"/>
      </g>
      <text class="department condensed" x="143" y="223" text-anchor="middle" font-size="19" font-weight="600" fill="var(--ink-grey)" letter-spacing="0.4">SCHOONHEIDSINSTITUUT</text>

      <g class="contact-rules" stroke="var(--rule)" stroke-width="0.5">
        <line x1="25" y1="288" x2="261" y2="288"/>
        <line x1="25" y1="302" x2="261" y2="302"/>
        <line x1="25" y1="330" x2="261" y2="330"/>
      </g>
      <g class="contact sans" font-size="8.5" fill="var(--ink-soft)" text-anchor="middle" font-weight="300">
        <text x="143" y="298">www.maisonk.be</text>
        <text x="143" y="313">enkel op afspraak, boek online</text>
        <text x="143" y="325">0486 91 37 52</text>
      </g>
      <g class="socials sans" font-size="6.5" fill="var(--ink-soft)" text-anchor="middle">
        <text x="105" y="379">instagram</text>
        <text x="143" y="379">facebook</text>
        <text x="180" y="379">tiktok</text>
      </g>

      <text class="brand-name sans" x="143" y="466" text-anchor="middle" font-size="20" font-weight="400" fill="var(--ink-light)" letter-spacing="2">ZOW</text>
      <text class="brand-sub sans" x="143" y="484" text-anchor="middle" font-size="6" font-weight="400" fill="var(--ink-soft)" letter-spacing="2">CLINIC</text>
      <text class="brand-line sans" x="143" y="507" text-anchor="middle" font-size="5.5" font-weight="400" fill="var(--ink-soft)" letter-spacing="1.2">PERMANENT MAKE UP BY LOTTE VERBEKE</text>
      <text class="department condensed" x="143" y="566" text-anchor="middle" font-size="19" font-weight="600" fill="var(--ink-grey)" letter-spacing="0.4">PERMANENT MAKE UP</text>

      <g class="contact-rules" stroke="var(--rule)" stroke-width="0.5">
        <line x1="25" y1="636" x2="261" y2="636"/>
        <line x1="25" y1="650" x2="261" y2="650"/>
        <line x1="25" y1="679" x2="261" y2="679"/>
      </g>
      <g class="contact sans" font-size="8.5" fill="var(--ink-soft)" text-anchor="middle" font-weight="300">
        <text x="143" y="646">www.zowclinic.be</text>
        <text x="143" y="661">gratis advies enkel op afspraak</text>
        <text x="143" y="674">0486 91 37 52</text>
      </g>
    </svg>
  </section>
</main>
</body>
</html>
```